Varro's Electrical & Solar Corflute Signage Design

So my plan is to put this design onto a 600 by 400 corflute sign (this sign will be printed out and cable tied to a fence FYI). I would like to have the name and the icon stand out. I need Varro's Electrical & Solar to be big and clear and I would like to have my "S" icon faded behind "Varro's Electrical & Solar" in the background.

I want to have my Lic No. - Top left with my ABN directly underneath. (I Want two ticks infront of them like this)
✓ Lic No. 582164K
✓ ABN 41 276 519 683

I want to have written on it: ALL ASPECTS OF ELECTRICAL (please use cool fonts and nothing too plain)
I also want to have: YOUR LOCAL TRUSTED ELECTRICIAN but if it looks too dicky then just have "all aspects of electrical" and just "free quotes • fast service" somewhere.
Directly underneath (smaller but still clear): FREE QUOTES • FAST SERVICE

At the bottom, I need my phone number big and clear - 0438 617 905 I would like this on a banner meaning like a cool strip at the bottom. (Please make the strip/banner look cool and not boring. Maybe shade the colour or something)
I also want the Facebook & Instagram icons on there so people can look us up on facebook & Instagram (make them match the colour of my logo or you could try any other colour that works)
Thank you so much!!

Colors

Designer to choose colors to be used in the design.

Requirements
Should not have
• no different colours other then the colours on my logo and icon

```html
<!DOCTYPE html>
<html lang="en">
<head>
<meta charset="utf-8">
<title>Varro's Electrical &amp; Solar – Corflute Sign</title>
<link href="https://fonts.googleapis.com/css2?family=Orbitron:wght@900&family=Michroma&family=Montserrat:ital,wght@0,600;0,800;1,600&display=swap" rel="stylesheet">
<style>
  :root {
    --page: #ffffff;
    --sign-dark: #020503;
    --sign-deep: #0b1f10;
    --green: #22c63e;
    --green-dark: #0a5a1a;
    --silver: #d9dcdc;
    --white: #ffffff;
  }
  * { margin: 0; padding: 0; box-sizing: border-box; }
  html, body { width: 1200px; height: 1166px; overflow: hidden; background: var(--page); }
  .canvas { position: relative; width: 1200px; height: 1166px; }
  .sign {
    position: absolute; left: 100px; top: 248px; width: 985px; height: 655px;
    background: radial-gradient(ellipse at 50% 40%, var(--sign-deep) 0%, var(--sign-dark) 75%);
    font-family: "Montserrat", sans-serif; color: var(--white); overflow: hidden;
  }
  .credentials { position: absolute; left: 41px; top: 24px; list-style: none; font-size: 23px; letter-spacing: 0.06em; line-height: 34px; }
  .credentials li::before { content: "\2714"; margin-right: 14px; }
  .brand-name {
    position: absolute; left: 0; right: 0; top: 102px; text-align: center;
    font-family: "Orbitron", sans-serif; font-weight: 900; font-size: 112px;
    letter-spacing: 0.04em; color: var(--silver); line-height: 1;
  }
  .brand-trade {
    position: absolute; left: 0; right: 0; top: 236px; text-align: center;
    font-family: "Michroma", sans-serif; font-size: 28px; letter-spacing: 0.22em; color: var(--silver);
  }
  .tagline {
    position: absolute; left: 0; right: 0; text-align: center; line-height: 1;
  }
  .tagline--headline { top: 322px; font-style: italic; font-weight: 600; font-size: 36px; letter-spacing: 0.17em; }
  .tagline--services { top: 376px; font-weight: 800; font-size: 31px; letter-spacing: 0.08em; }
  .tagline--sectors { top: 413px; font-weight: 800; font-size: 30px; letter-spacing: 0.08em; color: var(--green); }
  .tagline--offer { top: 448px; font-weight: 800; font-size: 30px; letter-spacing: 0.08em; color: var(--green); }
  .phone-banner { position: absolute; left: 40px; top: 540px; width: 640px; height: 90px; }
  .phone-number {
    position: absolute; left: 170px; top: 545px; font-weight: 800; font-size: 72px;
    letter-spacing: 0.04em; color: var(--silver); line-height: 80px;
  }
  .social { position: absolute; top: 558px; width: 64px; height: 64px; border-radius: 50%; background: var(--green); }
  .social--first { left: 788px; }
  .social--second { left: 866px; }
</style>
</head>
<body>
<main class="canvas">
  <section class="sign">
    <ul class="credentials">
      <li>Lic No. 582164K</li>
      <li>ABN 41 276 519 683</li>
    </ul>

    <h1 class="brand-name">VARRO'S</h1>
    <p class="brand-trade">ELECTRICAL &amp; SOLAR</p>

    <p class="tagline tagline--headline">ALL ASPECTS OF ELECTRICAL</p>
    <p class="tagline tagline--services">SOLAR INSTALLATION &amp; SOLUTIONS</p>
    <p class="tagline tagline--sectors">RESIDENTIAL • COMMERCIAL • INDUSTRIAL</p>
    <p class="tagline tagline--offer">FREE QUOTES • FAST SERVICE</p>

    <svg class="phone-banner" viewBox="0 0 640 90" aria-hidden="true">
      <defs>
        <linearGradient id="bannerFill" x1="0" y1="0" x2="0" y2="1">
          <stop offset="0" stop-color="#22c63e"/>
          <stop offset="1" stop-color="#0a5a1a"/>
        </linearGradient>
      </defs>
      <path d="M50 8 H635 L565 82 H50 Z" fill="url(#bannerFill)"/>
      <circle cx="53" cy="46" r="44" fill="#22c63e"/>
    </svg>
    <p class="phone-number">0438 617 905</p>

    <span class="social social--first" role="img" aria-label="Social page link"></span>
    <span class="social social--second" role="img" aria-label="Social page link"></span>
  </section>
</main>
</body>
</html>
```